About us:
Looking for eye catching cards for our 4D/HD Ultrasound Studio.

Description:
We are the premier 4D/HD Ultrasound studio in Pensacola/Pace as well as the greater panhandle area. We are a 4D/HD Ultrasound Studio in Pace, Florida, just a few minutes north of Pensacola. We offer 4D/HD imagining an early gender determination, 8 weeks by blood test and 14 weeks by ultrasound. We utilize the latest in 4D/HD technology to render beautiful images and memories that will last a lifetime.

At 4D Tiny Glimpse of Pace, we give a whole new meaning to ultrasounds. We utilize the most up-to-date 4D/HD ultrasound imaging, so we can provide clear, amazing images of your unborn baby to life. Will she have your nose or her Daddy's smile? Book your appointment today for an unforgettable experience. We also offer heartbeat animals.

Phone: 8505550147
www.4dtinyglimpse.example
address: 2716 -B HWY 38
Pace, FL 32590

Target Market(s)

Pregnant women

Requirements
Should not have
• Ultrasound training

```html
<!DOCTYPE html>
<html lang="en">
<head>
<meta charset="utf-8">
<title>4D Tiny Glimpse – Rack Cards</title>
<link rel="stylesheet" href="https://fonts.googleapis.com/css2?family=Poppins:wght@400;600;700&family=Kaushan+Script&display=swap">
<style>
  :root{
    --bg:#5c5c5c;
    --teal:#3bb8c9;
    --teal-dark:#1f6670;
    --teal-deep:#1a5a63;
    --ink:#1d1d1d;
    --red:#b01e2e;
    --white:#ffffff;
    --wash:#dcedf5;
    --pink:#ea5a6c;
    --gold:#d9b56a;
  }
  *{box-sizing:border-box;margin:0;padding:0}
  html,body{width:1200px;height:1200px;overflow:hidden;background:var(--bg)}
  body{position:relative;font-family:'Poppins',sans-serif;color:var(--ink)}

  .rack-card{
    position:absolute;top:162px;width:366px;height:820px;overflow:hidden;
    background:linear-gradient(180deg,#ffffff 0%,#eef6fa 40%,#e2f0f7 70%,#ffffff 88%);
    box-shadow:0 18px 30px rgba(0,0,0,.35);
  }
  .rack-card--front{left:137px}
  .rack-card--back{left:598px}

  .brand{position:absolute;left:22px;top:22px;display:flex;align-items:center;gap:8px;z-index:5}
  .brand__dot{width:16px;height:16px;border-radius:50%;background:var(--teal-dark)}
  .brand__name{font-family:'Poppins',sans-serif;font-weight:600;font-size:15px;color:var(--teal-dark);line-height:1}

  .hero-circle{
    position:absolute;left:106px;top:54px;width:468px;height:468px;border-radius:50%;
    border:6px solid var(--teal);
    background:radial-gradient(circle at 60% 45%,#6c7478 0%,#b9c1c5 35%,#3c3f44 70%,#d9dcdd 100%);
  }
  .face-ring{
    position:absolute;border-radius:50%;border:5px solid var(--teal);
    background:radial-gradient(circle at 50% 45%,#c98a78 0%,#a75a47 55%,#6e2a1f 100%);
    box-shadow:0 0 0 2px #fff;
  }
  .face-ring--one{left:203px;top:22px;width:130px;height:130px}
  .face-ring--two{left:31px;top:153px;width:134px;height:134px}
  .face-ring--three{left:60px;top:353px;width:142px;height:142px}

  .booking-badge{
    position:absolute;width:120px;height:120px;border-radius:50%;
    background:var(--teal-dark);
    box-shadow:0 0 0 5px #fff,0 0 0 8px #c9cfd2,0 6px 10px rgba(0,0,0,.35);
    display:flex;align-items:center;justify-content:center;z-index:6;
  }
  .booking-badge::before{
    content:"";position:absolute;inset:8px;border-radius:50%;border:1.5px dashed rgba(255,255,255,.8);
  }
  .booking-badge__text{color:#fff;font-weight:700;text-align:center;font-size:13px;line-height:1.4}
  .booking-badge__text span{display:block;font-size:15px}
  .rack-card--front .booking-badge{left:221px;top:456px}
  .rack-card--back .booking-badge{left:222px;top:435px}

  .section-title{position:absolute;left:23px;font-family:'Kaushan Script',cursive;color:var(--red);font-size:17px;line-height:1}
  .body-copy{position:absolute;left:23px;font-size:9.6px;line-height:13.8px;color:var(--ink);letter-spacing:-0.15px}
  .body-copy--intro{font-size:10.2px;line-height:14px;letter-spacing:0}
  .body-copy--justify{text-align:justify;width:322px}

  .bottom-band{position:absolute;left:0;top:0;width:366px;height:820px;z-index:3}
  .contact{position:absolute;left:22px;top:748px;z-index:7;list-style:none}
  .contact li{display:flex;align-items:center;gap:7px;color:#fff;font-size:12px;height:21.5px}
  .contact svg{width:12px;height:12px;flex:none}

  .partner-badge{
    position:absolute;left:235px;top:696px;width:108px;height:108px;border-radius:50%;
    background:var(--pink);border:4px solid var(--gold);box-shadow:0 0 0 2px #fff;z-index:7;
  }

  .lifestyle-photo{position:absolute;left:0;top:0;width:366px;height:520px;z-index:1}
  .snap{
    position:absolute;border:5px solid var(--teal);
    background:radial-gradient(circle at 50% 45%,#c98a78 0%,#9a4d3c 60%,#3b1510 100%);
    box-shadow:0 3px 6px rgba(0,0,0,.3);z-index:2;
  }
  .snap--a{left:80px;top:150px;width:82px;height:76px;transform:rotate(8deg)}
  .snap--b{left:15px;top:200px;width:88px;height:76px;transform:rotate(-6deg)}
  .snap--c{left:28px;top:265px;width:90px;height:82px;transform:rotate(-3deg)}
  .badge-clearance{float:right;width:134px;height:42px}
</style>
</head>
<body>

<!-- Front card -->
<section class="rack-card rack-card--front">
  <div class="brand"><span class="brand__dot"></span><span class="brand__name">4D Tiny Glimpse</span></div>

  <div class="hero-circle" role="img" aria-label="Photo of a sonographer performing a 3D ultrasound scan in front of a monitor"></div>
  <div class="face-ring face-ring--one" role="img" aria-label="4D ultrasound image of an unborn baby"></div>
  <div class="face-ring face-ring--two" role="img" aria-label="4D ultrasound image of an unborn baby"></div>
  <div class="face-ring face-ring--three" role="img" aria-label="4D ultrasound image of an unborn baby"></div>

  <div class="booking-badge"><p class="booking-badge__text">BOOKING<br>ONLINE<span>24/7</span></p></div>

  <h2 class="section-title" style="top:494px">About Us :</h2>
  <p class="body-copy body-copy--intro" style="top:517px">We are the premier 4D/HD<br>Ultrasound in Pensacola/Pace as<br>well as the greater pan-handle area.</p>

  <h2 class="section-title" style="top:574px">Description :</h2>
  <p class="body-copy body-copy--justify" style="top:594px">We are the premier 4D/HD Ultrasound studio in Pensacola/Pace as well as the greater panhandle area. We are a 4D/HD Ultrasound Studio in Pace, Florida, just a few minutes north of Pensacola. We offer 4D/HD imagining an early gender determination, 8 weeks by blood test and 14 weeks by ultrasound. We utilize the latest in 4D/HD technology to render beautiful images and memories that will last a lifetime.</p>

  <svg class="bottom-band" viewBox="0 0 366 820" aria-hidden="true">
    <path d="M0 697 C120 730 250 735 366 705 L366 719 C250 748 120 745 0 711Z" fill="var(--teal)"/>
    <path d="M0 716 C120 752 250 752 366 724 L366 820 L0 820Z" fill="var(--teal-deep)"/>
  </svg>

  <ul class="contact">
    <li><svg viewBox="0 0 24 24"><path fill="var(--teal)" d="M6.6 10.8a15.1 15.1 0 0 0 6.6 6.6l2.2-2.2c.3-.3.7-.4 1-.2 1.1.4 2.3.6 3.6.6.6 0 1 .4 1 1V20c0 .6-.4 1-1 1A17 17 0 0 1 3 4c0-.6.4-1 1-1h3.5c.6 0 1 .4 1 1 0 1.3.2 2.5.6 3.6.1.3 0 .7-.2 1z"/></svg>8505550147</li>
    <li><svg viewBox="0 0 24 24"><circle cx="12" cy="12" r="9" fill="none" stroke="var(--teal)" stroke-width="2"/><path d="M3 12h18M12 3c3 3 3 15 0 18M12 3c-3 3-3 15 0 18" fill="none" stroke="var(--teal)" stroke-width="1.6"/></svg>www.4dtinyglimpse.example</li>
    <li><svg viewBox="0 0 24 24"><path d="M12 2a6 6 0 0 0-6 6c0 4.5 6 11 6 11s6-6.5 6-11a6 6 0 0 0-6-6z" fill="none" stroke="var(--teal)" stroke-width="2"/><circle cx="12" cy="8" r="2" fill="var(--teal)"/><path d="M5 21h14" stroke="var(--teal)" stroke-width="2"/></svg>2716 -B HWY 38 Pace, FL 32590</li>
  </ul>
  <div class="partner-badge" aria-hidden="true"></div>
</section>

<!-- Back card -->
<section class="rack-card rack-card--back">
  <svg class="lifestyle-photo" viewBox="0 0 366 520" aria-hidden="true">
    <defs>
      <linearGradient id="photoTone" x1="0" y1="0" x2="1" y2="1">
        <stop offset="0" stop-color="#efe6e4"/>
        <stop offset=".55" stop-color="#e9dcdb"/>
        <stop offset="1" stop-color="#8d8585"/>
      </linearGradient>
    </defs>
    <path d="M0 0 H366 V468 C300 500 200 505 120 470 C70 448 30 420 0 380 Z" fill="url(#photoTone)"/>
    <path d="M0 380 C30 420 70 448 120 470 C200 505 300 500 366 468" fill="none" stroke="#fff" stroke-width="4"/>
    <path d="M0 388 C30 428 70 458 120 480 C200 515 300 510 366 478" fill="none" stroke="var(--teal)" stroke-width="5"/>
  </svg>
  <div role="img" aria-label="Photo of a pregnant woman in a white top holding an ultrasound print" style="position:absolute;left:0;top:0;width:366px;height:470px;z-index:1"></div>
  <div class="snap snap--a" role="img" aria-label="4D ultrasound image of an unborn baby"></div>
  <div class="snap snap--b" role="img" aria-label="4D ultrasound image of an unborn baby"></div>
  <div class="snap snap--c" role="img" aria-label="4D ultrasound image of an unborn baby"></div>

  <div class="brand"><span class="brand__dot"></span><span class="brand__name">4D Tiny Glimpse</span></div>

  <div class="booking-badge"><p class="booking-badge__text">BOOKING<br>ONLINE<span>24/7</span></p></div>

  <h2 class="section-title" style="top:513px">General Information :</h2>
  <p class="body-copy body-copy--justify" style="top:537px"><span class="badge-clearance"></span>At 4D Tiny Glimpse, we give a whole new meaning to ultrasounds. In the past, expectant parents were unable to see their baby until he or she was born; but now, 4D Tiny Glimpse provides revolutionary, elective 4D/HD prenatal ultrasound services and provides expectant parents with images to be treasured for a lifetime. We utilize the most up-to-date 4D/HD sonographic technology so that we are able to bring clear, amazing images of your unborn baby to life. Will she have your nose or her Daddy's smile? Book your appointment today for an unforgettable experience.</p>

  <svg class="bottom-band" viewBox="0 0 366 820" aria-hidden="true">
    <path d="M0 697 C120 730 250 735 366 705 L366 719 C250 748 120 745 0 711Z" fill="var(--teal)"/>
    <path d="M0 716 C120 752 250 752 366 724 L366 820 L0 820Z" fill="var(--teal-deep)"/>
  </svg>

  <ul class="contact">
    <li><svg viewBox="0 0 24 24"><path fill="var(--teal)" d="M6.6 10.8a15.1 15.1 0 0 0 6.6 6.6l2.2-2.2c.3-.3.7-.4 1-.2 1.1.4 2.3.6 3.6.6.6 0 1 .4 1 1V20c0 .6-.4 1-1 1A17 17 0 0 1 3 4c0-.6.4-1 1-1h3.5c.6 0 1 .4 1 1 0 1.3.2 2.5.6 3.6.1.3 0 .7-.2 1z"/></svg>8505550147</li>
    <li><svg viewBox="0 0 24 24"><circle cx="12" cy="12" r="9" fill="none" stroke="var(--teal)" stroke-width="2"/><path d="M3 12h18M12 3c3 3 3 15 0 18M12 3c-3 3-3 15 0 18" fill="none" stroke="var(--teal)" stroke-width="1.6"/></svg>www.4dtinyglimpse.example</li>
    <li><svg viewBox="0 0 24 24"><path d="M12 2a6 6 0 0 0-6 6c0 4.5 6 11 6 11s6-6.5 6-11a6 6 0 0 0-6-6z" fill="none" stroke="var(--teal)" stroke-width="2"/><circle cx="12" cy="8" r="2" fill="var(--teal)"/><path d="M5 21h14" stroke="var(--teal)" stroke-width="2"/></svg>2716 -B HWY 38 Pace, FL 32590</li>
  </ul>
  <div class="partner-badge" aria-hidden="true"></div>
</section>

</body>
</html>
```